Hi,
We are an accounting firm looking to upgrade the following:
Logo, letterhead, withcomp slips and maybe our business cards. I have attached our original letterhead (sample A) and a letterhead (SAmple B) which we like the design and layout, however I want to stick with the colours of our orginal letterhead (Sample A) but improve and modernise the look with other letter head (Sample B) I have attached both. On the footer of Sample A, we would like to remove the names of the directors but leave EST. 1985 we also want to add the QRT logo ABN and TAX AGENT logo as stated in Sample B , we would like to do a layout for the header similar to SAmple B however maybe a bit more structured.

```html
<!DOCTYPE html>
<html lang="en">
<head>
<meta charset="utf-8">
<title>Brentholm Accountants — Stationery Set</title>
<link rel="stylesheet" href="https://fonts.googleapis.com/css2?family=Montserrat:wght@400;500;600;700&display=swap">
<style>
  :root {
    --backdrop: #8a8b8d;
    --navy: #163a6e;
    --navy-mid: #1f4f8c;
    --blue: #2b67a8;
    --sky: #3a86c8;
    --panel-black: #1e1e1e;
    --card-back: #0c4a82;
    --paper: #ffffff;
    --ink-light: #ffffff;
  }
  * { box-sizing: border-box; margin: 0; padding: 0; }
  html, body { width: 1200px; height: 1200px; overflow: hidden; }
  body {
    background: var(--backdrop);
    font-family: "Montserrat", sans-serif;
    color: var(--ink-light);
    position: relative;
  }
  .sheet, .card { position: absolute; box-shadow: 6px 8px 14px rgba(0,0,0,.35); overflow: hidden; }
  .shapes { position: absolute; inset: 0; width: 100%; height: 100%; display: block; }
  .abs { position: absolute; white-space: nowrap; line-height: 1; }

  /* Wordmark */
  .wordmark { position: absolute; font-weight: 600; letter-spacing: -0.5px; white-space: nowrap; }
  .wordmark .name { display: block; line-height: 1; }
  .wordmark .sub { display: flex; align-items: center; line-height: 1; }
  .wordmark .sub::before { content: ""; display: inline-block; background: var(--ink-light); }

  /* Letterhead */
  .letterhead { left: 75px; top: 75px; width: 744px; height: 1050px; background: var(--paper); }
  .letterhead .wordmark { left: 91px; top: 41px; }
  .letterhead .wordmark .name { font-size: 40px; }
  .letterhead .wordmark .sub { font-size: 21px; margin-top: 9px; margin-left: 9px; }
  .letterhead .wordmark .sub::before { width: 17px; height: 17px; margin-right: 23px; }

  .tagline { text-align: right; font-weight: 400; }
  .letterhead .tagline { right: 38px; top: 52px; font-size: 16px; line-height: 20px; }

  .contact-list { position: absolute; list-style: none; white-space: nowrap; }
  .contact-list li { display: flex; align-items: center; }
  .contact-list svg { flex: none; fill: var(--ink-light); }
  .letterhead .contact-list { left: 33px; top: 931px; font-size: 16px; }
  .letterhead .contact-list li { height: 25.3px; }
  .letterhead .contact-list svg { width: 15px; height: 15px; margin-right: 15px; }

  .abn { font-weight: 400; }
  .letterhead .abn { left: 300px; top: 944px; font-size: 17px; }

  .entity { text-align: right; }
  .entity .company { font-weight: 500; }
  .entity .line { display: flex; justify-content: flex-end; align-items: center; }
  .entity .pin { fill: var(--ink-light); margin-left: 6px; }
  .letterhead .entity { right: 38px; top: 910px; font-size: 16px; }
  .letterhead .entity .company { margin-bottom: 8px; }
  .letterhead .entity .line { height: 21px; }
  .letterhead .entity .line.no-pin { padding-right: 16px; }
  .letterhead .entity .pin { width: 10px; height: 13px; }

  /* Business card front */
  .card-front { left: 601px; top: 244px; width: 500px; height: 287px; }
  .card-front .wordmark { left: 29px; top: 37px; }
  .card-front .wordmark .name { font-size: 31px; }
  .card-front .wordmark .sub { font-size: 18px; margin-top: 6px; margin-left: 7px; }
  .card-front .wordmark .sub::before { width: 13px; height: 13px; margin-right: 19px; }
  .card-front .tagline { right: 26px; top: 35px; font-size: 13px; line-height: 16px; }
  .card-front .tagline .small { font-size: 11.5px; }
  .person { position: absolute; left: 29px; top: 140px; }
  .person .name { font-size: 19px; font-weight: 700; letter-spacing: .3px; line-height: 1; }
  .person .role { font-size: 14px; font-weight: 400; margin-top: 4px; }
  .card-front .contact-list { left: 34px; top: 190px; font-size: 10.8px; }
  .card-front .contact-list li { height: 20px; }
  .card-front .contact-list svg { width: 10px; height: 10px; margin-right: 12px; }
  .card-front .abn { right: 26px; top: 124px; font-size: 14px; }
  .card-front .entity { right: 21px; top: 186px; font-size: 13px; }
  .card-front .entity .company { margin-bottom: 6px; font-size: 12px; }
  .card-front .entity .line { height: 17px; }
  .card-front .entity .line.no-pin { padding-right: 13px; }
  .card-front .entity .pin { width: 7px; height: 9px; }

  /* Business card back */
  .card-back { left: 601px; top: 600px; width: 500px; height: 287px; background: var(--card-back); }
  .card-back .wordmark { left: 50%; top: 50%; transform: translate(-50%, -50%); }
  .card-back .wordmark .name { font-size: 42px; }
  .card-back .wordmark .sub { font-size: 22px; margin-top: 9px; margin-left: 9px; }
  .card-back .wordmark .sub::before { width: 18px; height: 18px; margin-right: 22px; }
</style>
</head>
<body>

<svg width="0" height="0" style="position:absolute" aria-hidden="true">
  <defs>
    <symbol id="icon-phone" viewBox="0 0 16 16"><path d="M3.6 1.2l2.3 2.4-1.3 1.9c.9 2 2.5 3.6 4.5 4.6l1.9-1.3 2.4 2.3-1.4 2.4C6.9 13.1 2.9 9.1 1.3 3.1z"/></symbol>
    <symbol id="icon-fax" viewBox="0 0 16 16"><path d="M4 1h8v4H4zM1 6h14v7h-3v-3H4v3H1zM5 11h6v4H5z"/></symbol>
    <symbol id="icon-mail" viewBox="0 0 16 16"><path d="M1 3h14v1L8 9 1 4zM1 5.5l7 5 7-5V13H1z"/></symbol>
    <symbol id="icon-web" viewBox="0 0 16 16"><path d="M8 1a7 7 0 100 14A7 7 0 008 1zm0 2a2 2 0 110 4 2 2 0 010-4zM4.5 9a1.5 1.5 0 110 3 1.5 1.5 0 010-3zm7 0a1.5 1.5 0 110 3 1.5 1.5 0 010-3z"/></symbol>
    <symbol id="icon-pin" viewBox="0 0 10 13"><path d="M5 0a4 4 0 00-4 4c0 3 4 9 4 9s4-6 4-9a4 4 0 00-4-4zm0 2.3a1.7 1.7 0 110 3.4 1.7 1.7 0 010-3.4z"/></symbol>
    <linearGradient id="grad-navy" x1="0" y1="0" x2="1" y2="0">
      <stop offset="0" stop-color="#1a4377"/>
      <stop offset="1" stop-color="#2d6cb0"/>
    </linearGradient>
    <linearGradient id="grad-card" x1="0" y1="0" x2="1" y2="0.4">
      <stop offset="0" stop-color="#18407a"/>
      <stop offset="1" stop-color="#2a64a6"/>
    </linearGradient>
  </defs>
</svg>

<!-- Letterhead -->
<section class="sheet letterhead">
  <svg class="shapes" viewBox="0 0 595 840" preserveAspectRatio="none" aria-hidden="true">
    <polygon points="0,0 595,0 595,82 300,82 242,146 0,146" fill="url(#grad-navy)"/>
    <polygon points="318,32 595,32 595,82 300,82 242,146 0,146 0,138 236,138" fill="var(--sky)"/>
    <polygon points="0,738 196,738 224,708 595,708 595,840 0,840" fill="url(#grad-navy)"/>
    <polygon points="192,734 222,704 440,704 440,712 228,712 200,740 0,740 0,734" fill="var(--sky)"/>
    <polygon points="262,745 430,745 400,778 232,778" fill="var(--sky)"/>
    <polygon points="430,705 595,705 595,817 345,817" fill="var(--panel-black)"/>
  </svg>

  <div class="wordmark">
    <span class="name">Brentholm</span>
    <span class="sub">Accountants</span>
  </div>
  <div class="abs tagline">EST. 1985<br>Certified Practising Accountants</div>

  <ul class="contact-list">
    <li><svg><use href="#icon-phone"/></svg>+61 3 9412 7830</li>
    <li><svg><use href="#icon-fax"/></svg>+61 3 9412 7831</li>
    <li><svg><use href="#icon-mail"/></svg>info@brentholm.com.au</li>
    <li><svg><use href="#icon-web"/></svg>www.brentholmaccountants.com.au</li>
  </ul>
  <div class="abs abn">ABN 41 527 308 916</div>
  <div class="abs entity">
    <div class="company">BRENTHOLM PTY LTD</div>
    <div class="line">482 Garnet Street<svg class="pin"><use href="#icon-pin"/></svg></div>
    <div class="line no-pin">Elsternwick, Vic. 3185</div>
    <div class="line no-pin">Australia</div>
  </div>
</section>

<!-- Business card, front -->
<section class="card card-front">
  <svg class="shapes" viewBox="0 0 400 229" preserveAspectRatio="none" aria-hidden="true">
    <rect width="400" height="229" fill="url(#grad-card)"/>
    <polygon points="0,0 400,0 400,55 213,55 185,97 0,97" fill="#173c72"/>
    <polygon points="232,23 400,23 400,55 213,55 185,97 0,97 0,92 180,92" fill="var(--sky)"/>
    <polygon points="216,200 253,158 261,158 224,200" fill="var(--sky)"/>
    <polygon points="263,138 400,138 400,213 213,213" fill="var(--panel-black)"/>
  </svg>

  <div class="wordmark">
    <span class="name">Brentholm</span>
    <span class="sub">Accountants</span>
  </div>
  <div class="abs tagline">EST. 1985<br><span class="small">Certified Practising Accountants</span></div>

  <div class="person">
    <div class="name">YOUR NAME</div>
    <div class="role">Founder &amp; Director</div>
  </div>
  <ul class="contact-list">
    <li><svg><use href="#icon-phone"/></svg>+61 3 9412 7830</li>
    <li><svg><use href="#icon-fax"/></svg>+61 3 9412 7831</li>
    <li><svg><use href="#icon-mail"/></svg>info@brentholm.com.au</li>
    <li><svg><use href="#icon-web"/></svg>www.brentholmaccountants.com.au</li>
  </ul>
  <div class="abs abn">ABN 41 527 308 916</div>
  <div class="abs entity">
    <div class="company">BRENTHOLM PTY LTD</div>
    <div class="line">482 Garnet Street<svg class="pin"><use href="#icon-pin"/></svg></div>
    <div class="line no-pin">Elsternwick, Vic. 3185</div>
    <div class="line no-pin">Australia</div>
  </div>
</section>

<!-- Business card, back -->
<section class="card card-back">
  <div class="wordmark">
    <span class="name">Brentholm</span>
    <span class="sub">Accountants</span>
  </div>
</section>

</body>
</html>
```